Marlow Guard Shop Signage with provided LOGO

Need 2 designs (1) indicating the store is around the corner horizontal format and (1) in a vertical format without the around the corner indication. HD image for a 24" by 60" sign. Use attached image for inspiration. Our business of on the south side of a large building and we need to have 2 signs on the front of the build indicating LEFT and the last sign will be a sidewalk sign next to our business.

Industry/Entity Type

Security

Font styles to use
Serif

Colors
33a6d7

Requirements
Must have
• WEBSITE URL: www.dwellsafedepot.com and www.marlowguardshop.com they can be in small font.
Nice to have
• Phone Number (833) 562-9184

```html
<!DOCTYPE html>
<html lang="en">
<head>
<meta charset="utf-8">
<title>Marlow Guard Shop – Signage</title>
<link rel="stylesheet" href="https://fonts.googleapis.com/css2?family=Oswald:wght@500;600&family=Roboto:wght@400;700&display=swap">
<style>
  :root {
    --page-bg: #ececec;
    --banner-top: #2196d6;
    --banner-bottom: #174c9c;
    --panel-white: #ffffff;
    --ring-black: #111111;
    --ring-silver: #b9bec4;
    --brand-blue: #1e77c6;
    --text-white: #ffffff;
  }
  html, body {
    margin: 0;
    padding: 0;
    width: 1200px;
    height: 1200px;
    overflow: hidden;
    background: var(--page-bg);
  }
  .canvas {
    position: relative;
    width: 1200px;
    height: 1200px;
  }
  .banner {
    position: absolute;
    top: 77px;
    width: 412px;
    height: 1030px;
    box-shadow: 0 6px 18px rgba(0,0,0,0.25);
  }
  .banner--vertical { left: 118px; }
  .banner--directional { left: 682px; }
  .brand-name {
    font-family: "Oswald", "Arial Narrow", sans-serif;
    font-weight: 600;
    fill: var(--brand-blue);
  }
  .phone {
    font-family: "Roboto", Arial, sans-serif;
    font-weight: 700;
    fill: var(--text-white);
  }
  .web {
    font-family: "Roboto", Arial, sans-serif;
    font-weight: 400;
    fill: var(--text-white);
  }
</style>
</head>
<body>
<div class="canvas">

  <!-- Vertical sidewalk sign -->
  <svg class="banner banner--vertical" viewBox="0 0 412 1030" aria-label="Marlow Guard Shop vertical sign">
    <defs>
      <linearGradient id="bannerFillA" x1="0" y1="0" x2="0" y2="1">
        <stop offset="0" stop-color="var(--banner-top)"/>
        <stop offset="1" stop-color="var(--banner-bottom)"/>
      </linearGradient>
      <clipPath id="bannerClipA"><rect width="412" height="1030"/></clipPath>
    </defs>
    <g clip-path="url(#bannerClipA)">
      <rect class="banner-field" width="412" height="1030" fill="url(#bannerFillA)"/>
      <ellipse class="panel-ring-silver" cx="206" cy="420" rx="352" ry="334" fill="var(--ring-silver)"/>
      <ellipse class="panel-ring-black" cx="206" cy="420" rx="346" ry="328" fill="var(--ring-black)"/>
      <ellipse class="panel-ring-silver-inner" cx="206" cy="420" rx="341" ry="323" fill="var(--ring-silver)"/>
      <ellipse class="panel-white" cx="206" cy="420" rx="338" ry="320" fill="var(--panel-white)"/>
    </g>
    <circle class="brand-mark" cx="206" cy="320" r="78" fill="var(--brand-blue)"/>
    <text class="brand-name" x="206" y="532" font-size="76" text-anchor="middle">MARLOW</text>
    <text class="brand-name" x="206" y="598" font-size="44" text-anchor="middle">GUARD SHOP</text>
    <text class="phone" x="206" y="858" font-size="40" text-anchor="middle">(833) 562-9184</text>
    <text class="web" x="206" y="905" font-size="18" text-anchor="middle">www.dwellsafedepot.com</text>
    <text class="web" x="206" y="929" font-size="18" text-anchor="middle">www.marlowguardshop.com</text>
  </svg>

  <!-- Directional sign pointing left -->
  <svg class="banner banner--directional" viewBox="0 0 412 1030" aria-label="Marlow Guard Shop directional sign">
    <defs>
      <linearGradient id="bannerFillB" x1="0" y1="0" x2="0" y2="1">
        <stop offset="0" stop-color="var(--banner-top)"/>
        <stop offset="1" stop-color="var(--banner-bottom)"/>
      </linearGradient>
      <clipPath id="bannerClipB"><rect width="412" height="1030"/></clipPath>
    </defs>
    <g clip-path="url(#bannerClipB)">
      <rect class="banner-field" width="412" height="1030" fill="url(#bannerFillB)"/>
      <ellipse class="panel-ring-silver" cx="206" cy="400" rx="352" ry="324" fill="var(--ring-silver)"/>
      <ellipse class="panel-ring-black" cx="206" cy="400" rx="346" ry="318" fill="var(--ring-black)"/>
      <ellipse class="panel-ring-silver-inner" cx="206" cy="400" rx="341" ry="313" fill="var(--ring-silver)"/>
      <ellipse class="panel-white" cx="206" cy="400" rx="338" ry="310" fill="var(--panel-white)"/>
    </g>
    <circle class="brand-mark" cx="206" cy="320" r="78" fill="var(--brand-blue)"/>
    <text class="brand-name" x="206" y="532" font-size="76" text-anchor="middle">MARLOW</text>
    <text class="brand-name" x="206" y="598" font-size="44" text-anchor="middle">GUARD SHOP</text>
    <text class="phone" x="206" y="824" font-size="40" text-anchor="middle">(833) 562-9184</text>
    <text class="web" x="206" y="866" font-size="18" text-anchor="middle">www.dwellsafedepot.com</text>
    <text class="web" x="206" y="890" font-size="18" text-anchor="middle">www.marlowguardshop.com</text>
    <g class="direction-arrow" fill="var(--text-white)">
      <polygon points="65,946 104,912 104,933 272,933 272,959 104,959 104,980"/>
      <rect x="278" y="933" width="5" height="26"/>
      <rect x="289" y="933" width="5" height="26"/>
      <rect x="300" y="933" width="34" height="26"/>
    </g>
  </svg>

</div>
</body>
</html>
```